Design refresh required for educational resources

A full redesign/refresh is required for an education resource kit.
The final outputs will include:
- Powerpoint slide template
- parent handout template
- overview template
- 2 different types of lesson plan templates (can be related but need to have some differences to distinguish between the two)
- 2 x branded labels for resources
- teacher 'intervention plan' summary sheet
- 'scope and sequence' document
Design needs to have a fun, modern feel, capturing elements of the New Zealand landscape, flora and/or fauna.
The resources will be used as part of a teaching kit for use in schools.
Please see attached files for existing samples of some of the above documents. Full content to be provided for successful applicant.
Please submit sample of one or two of the documents to bid for this work - enough so that I can see the overall design aesthetic you are proposing.
New Zealand teachers and parents of 5 year old children

```html
<!DOCTYPE html>
<html lang="en">
<head>
<meta charset="utf-8">
<title>Parent Overview – Week 1</title>
<link href="https://fonts.googleapis.com/css2?family=Open+Sans:ital,wght@0,400;0,600;0,700;0,800;1,400&family=Arimo&display=swap" rel="stylesheet">
<style>
  :root {
    --purple: #4f2f7c;
    --purple-deep: #452a6f;
    --purple-text: #5a3a8c;
    --orange: #f0b25a;
    --orange-band: #efae55;
    --ink: #2b2b2b;
    --white: #ffffff;
    --line: #f0b25a;
  }
  * { box-sizing: border-box; margin: 0; padding: 0; }
  html, body { width: 921px; height: 1200px; overflow: hidden; background: var(--white); }
  body { font-family: "Open Sans", sans-serif; color: var(--ink); position: relative; }

  .masthead {
    position: absolute; left: 0; top: 0; width: 921px; height: 322px;
    background: linear-gradient(135deg, var(--purple) 0%, var(--purple-deep) 100%);
    overflow: hidden;
  }
  .week-badge {
    position: absolute; left: 50px; top: -110px; width: 218px; height: 218px;
    border-radius: 50%; background: var(--orange);
    box-shadow: 0 0 0 3px var(--purple), 0 0 0 4.5px #d9cbe8;
  }
  .week-label {
    position: absolute; left: 78px; top: 22px;
    font-weight: 800; font-size: 32px; letter-spacing: 1px; color: var(--purple);
    line-height: 56px;
  }
  .week-label .num { font-size: 48px; }
  .headline {
    position: absolute; left: 80px; top: 112px;
    font-weight: 700; font-size: 41px; line-height: 50px; color: var(--orange);
    white-space: nowrap;
  }
  .book-title {
    position: absolute; left: 80px; top: 224px;
    font-style: italic; font-size: 24px; line-height: 32px; color: var(--white);
    white-space: nowrap;
  }
  .book-author {
    position: absolute; left: 80px; top: 260px;
    font-size: 19px; line-height: 26px; color: var(--white);
  }
  .book-cover {
    position: absolute; left: 579px; top: 38px; width: 296px; height: 284px;
    background: linear-gradient(180deg, #c9a8cf 0%, #f3c9a0 38%, #6aa4d6 62%, #2b62ad 100%);
  }
  .accent-band { position: absolute; left: 0; top: 322px; width: 921px; height: 14px; background: var(--orange-band); }

  .panel {
    position: absolute; border: 1px solid var(--line); background: var(--white);
    border-radius: 14px 14px 0 0; overflow: hidden;
  }
  .panel-head {
    background: var(--orange);
    color: var(--purple-text); font-weight: 700; text-align: center;
    display: flex; align-items: center; justify-content: center;
  }
  .panel.words { left: 75px; top: 377px; width: 407px; height: 258px; }
  .panel.sounds { left: 502px; top: 377px; width: 341px; height: 258px; }
  .panel.words .panel-head, .panel.sounds .panel-head { height: 68px; font-size: 22px; line-height: 26px; }
  .word-list { padding: 10px 30px 0 18px; font-size: 15.5px; line-height: 22px; }
  .word-list p { margin-bottom: 5px; }
  .word-list strong { color: var(--purple-text); font-weight: 700; }
  .sound-list { padding: 16px 26px 0; font-family: "Arimo", sans-serif; font-size: 16.5px; line-height: 25px; }

  .panel.play { left: 75px; top: 659px; width: 772px; height: 403px; }
  .panel.play .panel-head { height: 50px; font-size: 22px; }
  .play-list { list-style: none; padding: 14px 12px 0 32px; font-size: 16px; line-height: 22px; }
  .play-list li { position: relative; margin-bottom: 4px; }
  .play-list li::before {
    content: ""; position: absolute; left: -16px; top: 8px; width: 5px; height: 5px;
    border-radius: 50%; background: var(--purple-text);
  }

  .footer-band { position: absolute; left: 0; top: 1126px; width: 921px; height: 74px; background: var(--purple); }
  .footer-note { position: absolute; left: 76px; top: 1140px; font-size: 15px; line-height: 21px; color: var(--white); }
  .footer-note .url { color: var(--orange); font-weight: 700; }
  .partner-strip {
    position: absolute; left: 606px; top: 1097px; width: 260px; height: 103px; background: var(--white);
    display: flex; align-items: center; justify-content: space-around; padding: 0 8px;
  }
  .partner { display: flex; flex-direction: column; align-items: center; gap: 6px;
    font-size: 11px; font-weight: 700; color: var(--purple); text-align: center; line-height: 13px; width: 110px; }
  .partner .mark { width: 26px; height: 26px; border-radius: 50%; background: #7bb241; }
  .partner .mark.square { border-radius: 0; background: #2b2b2b; }
  .partner-divider { width: 1px; height: 60px; background: #333; }
</style>
</head>
<body>
  <header class="masthead">
    <div class="week-badge"></div>
    <div class="week-label">WEEK <span class="num">1</span></div>
    <h1 class="headline">This week your<br>Child’s class is reading</h1>
    <p class="book-title">Captain Puddle Sails the Open Sea</p>
    <p class="book-author">By Harriet Lowe and Tama Reid</p>
    <div class="book-cover" role="img" aria-label="Cover image of this week's book"></div>
  </header>
  <div class="accent-band"></div>

  <section class="panel words">
    <h2 class="panel-head">Some new words<br>your child is learning</h2>
    <div class="word-list">
      <p><strong>Brave</strong> means to be ready to face danger and be courageous.</p>
      <p><strong>Depart</strong> is when somebody goes away or leaves.</p>
      <p>A <strong>breeze</strong> is a very light wind.</p>
      <p><strong>Hoist</strong> means to lift or haul something up using a mechanical device.</p>
    </div>
  </section>

  <section class="panel sounds">
    <h2 class="panel-head">Some new sounds<br>your child is learning</h2>
    <div class="sound-list">
      <p>'m' as in mud, man and moon</p>
      <p>'d' as in duck and dog</p>
    </div>
  </section>

  <section class="panel play">
    <h2 class="panel-head">Some fun ways you can play with sounds at home</h2>
    <ul class="play-list">
      <li>Use playdough, modelling clay, pipe cleaners or even blocks to make the shapes of this week's letters. Practice making the 'm' sound which you're creating your letters.</li>
      <li>Talk about how the letter looks, and then brainstorm some words that start with its sound. Your child may remember some of the words from class to start you off! When your child finds a word encourage them to say the name and the letter sound e.g. mug starts with an 'm' sound.</li>
      <li>Write the letters and have them around you home – draw your child's attention to them every time you see them and practice the sound.</li>
      <li>Hide objects or toys that start with the same letter as the one you are targeting and go on a 'letter' treasure hunt – see who can get the most of each letter. When they find them get them to yell out the sound!</li>
      <li>If you are reading a book with them see who can find any words that start with a 'm' or a 'd' the fastest. If they are able to, get them to read the word aloud, or support them in doing this. Practice making the 'm' or 'd' sound.</li>
    </ul>
  </section>

  <footer>
    <div class="footer-band"></div>
    <p class="footer-note">To access online versions of the small readers visit<br><span class="url">https://www.brightbeginningsreading.com/for-families</span></p>
    <div class="partner-strip">
      <div class="partner"><span class="mark"></span>Bright Beginnings Literacy</div>
      <div class="partner-divider"></div>
      <div class="partner"><span class="mark square"></span>Southern Plains University</div>
    </div>
  </footer>
</body>
</html>
```